11 x 17 Orvanthes Quote

Design the following quote in a poster.

"First say to yourself what you would be; then do what you have to do." - Orvanthes

See here for inspiration - https://prints.mornbrekal.com/

Quote

```html
<!DOCTYPE html>
<html lang="en">
<head>
<meta charset="utf-8">
<title>Orvanthes Quote Poster</title>
<link rel="stylesheet" href="https://fonts.googleapis.com/css2?family=Bebas+Neue&display=swap">
<style>
  :root {
    --paper: #ffffff;
    --ink: #1e1a18;
    --accent: #6876b8;
  }
  html, body {
    margin: 0;
    padding: 0;
    overflow: hidden;
    background: var(--paper);
  }
  .poster {
    position: relative;
    width: 927px;
    height: 1200px;
    background: var(--paper);
    font-family: "Bebas Neue", "Arial Narrow", sans-serif;
    overflow: hidden;
  }
  .quote-line {
    position: absolute;
    left: 0;
    width: 100%;
    margin: 0;
    text-align: center;
    font-size: 93px;
    line-height: 1;
    font-weight: 400;
    letter-spacing: 0.06em;
    word-spacing: 0.12em;
    color: var(--ink);
    white-space: nowrap;
  }
  .quote-line--accent { color: var(--accent); }
  .line-1 { top: 264px; }
  .line-2 { top: 385px; }
  .line-3 { top: 510px; }
  .line-4 { top: 631px; }
  .line-5 { top: 756px; }
  .rule {
    position: absolute;
    height: 6px;
    background: var(--accent);
  }
  .rule-1 { top: 474px; left: 239px; width: 438px; }
  .rule-2 { top: 840px; left: 141px; width: 642px; }
  .attribution {
    position: absolute;
    top: 1066px;
    left: 0;
    width: 100%;
    margin: 0;
    text-align: center;
    font-size: 58px;
    line-height: 1;
    letter-spacing: 0.03em;
    color: var(--ink);
  }
</style>
</head>
<body>
  <main class="poster">
    <blockquote>
      <p class="quote-line line-1">"First say</p>
      <p class="quote-line quote-line--accent line-2">to yourself</p>
      <div class="rule rule-1"></div>
      <p class="quote-line line-3">what you would be;</p>
      <p class="quote-line line-4">then do what</p>
      <p class="quote-line quote-line--accent line-5">you have to do<span style="color: var(--ink)">".</span></p>
      <div class="rule rule-2"></div>
    </blockquote>
    <p class="attribution">Orvanthes</p>
  </main>
</body>
</html>
```